依頼詳細
美容室ですが、美容室っぽさはデザインの中に取り込まなくても結構です。

イメージ的には、
堅苦しくなく、
家族や友人から送られてきたのかな??
と感じるような、
女性目線のデザイン性がありユーモアを感じさせるデザインが希望です。

裏面にスタッフ写真をうっすらと載せていただきたいです。また、オリジナル性を重視しますので、
ロゴもしくは店名(lumo.)をデザインの中に取り入れていただきたいです。

宜しくお願いいたします。
記載項目
表にはサロン名、もしくはロゴ。

裏には年末年始のあいさつ文、スタッフ写真、サロン詳細をよろしくお願いします。

希望イメージ
• +5 0 +5
• シンプル
複雑
• 単色
カラフル
• 暗い
明るい
• 日常
高級
• 遊び心
厳粛
• 未来的
伝統的
• 女性的
男性的
希望する色
水色系
納品ファイル
• フォトショップ形式 (.psd)
補足説明
サロンホームページ、ブログなどをご参照いただけれたらと思います。
http://maison-lumo.jp/

たくさんのご応募お待ちしております。

依頼公開後の追記内容
スタッフ写真、ロゴを添付いたしました。よろしくお願いします。
形式として

一面はビジュアルでクリスマスを意識。

もう一面にアドレスとご挨拶を記載していただきたいです。

昨年のクリスマスカードを添付いたしますのでご参考までに。
■ 選んだ理由

素敵な応募の数々、本当にありがとうございます。 まず、裏に書いてあるサロンの外装。 「私たちからの手紙」だと勘がいい方だと気付いてくれるかも?というお客様の顔が浮かび、作っていてとても楽しい気持ちになりました。 そして、表のセンスのいいユーモアとデザイン性、サロンのイメージカラーの水色もしっかりと反映してくださっている、そんなデザインに惚れました。 他にもかなり迷いましたが、スタッフ4人で投票した結果、こちらのkirapeko352さんの作品にさせていただきました。 沢山のご応募、本当にありがとうございました

■ 提案者全員のお礼・コメント

限られた時間の中、沢山の心のこもったデザインにすごく迷い、決めるのにかなり話し合いを要しました。 やっぱり、デザインは人を幸せにするなと。 僕らも、デザイナーとして沢山の人を幸せにするのを生業としております。 皆様の努力や知識が人々を笑顔にし、心を豊かにしている。 本当、デザイナーの力ってすごいです。 今回はクリスマスカードという企画のため、1つの作品を選ばせていただきましたが、他の企画ならこの方かな?というデザインもありました!ぜひまた皆様とお仕事が出来ればと考えております。 ありがとうございました

```html
<!DOCTYPE html>
<html lang="en">
<head>
<meta charset="utf-8">
<title>lumo. Holiday Card</title>
<link rel="stylesheet" href="https://fonts.googleapis.com/css2?family=Great+Vibes&family=Cinzel:wght@500&display=swap">
<style>
  :root {
    --paper: #f7f3ee;
    --ink: #4a4644;
    --frame: #eea596;
    --frame-soft: #f3bfb3;
    --mark: #aaa39d;
    --leaf: #9bb5a6;
    --bloom: #e9a89a;
    --petal: #cfc4b8;
  }
  html, body {
    margin: 0;
    padding: 0;
    overflow: hidden;
    background: var(--paper);
  }
  .card {
    position: relative;
    width: 840px;
    height: 1200px;
    background: var(--paper);
    overflow: hidden;
  }
  .card__frame,
  .card__florals {
    position: absolute;
    inset: 0;
    width: 840px;
    height: 1200px;
  }
  .greeting {
    position: absolute;
    left: 0;
    width: 840px;
    margin: 0;
    text-align: center;
    font-family: "Great Vibes", cursive;
    font-weight: 400;
    color: var(--ink);
    line-height: 1;
    white-space: nowrap;
  }
  .greeting--merry { top: 318px; font-size: 108px; }
  .greeting--christmas { top: 424px; font-size: 128px; }
  .greeting--and { top: 556px; font-size: 58px; }
  .greeting--newyear { top: 632px; font-size: 78px; }
  .signature {
    position: absolute;
    top: 806px;
    left: 0;
    width: 840px;
    display: flex;
    justify-content: center;
    align-items: center;
    gap: 16px;
    font-family: "Cinzel", serif;
    font-weight: 500;
    font-size: 44px;
    line-height: 1;
    color: var(--mark);
    letter-spacing: 1px;
  }
  .signature__dot {
    width: 26px;
    height: 26px;
    border-radius: 50%;
    background: var(--mark);
  }
</style>
</head>
<body>
<main class="card">
  <svg class="card__frame" viewBox="0 0 840 1200" aria-hidden="true">
    <path d="M146,238 H694 A40,40 0 0 0 734,278 V926 A40,40 0 0 0 694,966 H146 A40,40 0 0 0 106,926 V278 A40,40 0 0 0 146,238 Z"
          fill="none" stroke="var(--frame)" stroke-width="6"/>
    <path d="M160,254 H680 A34,34 0 0 0 718,292 V912 A34,34 0 0 0 680,950 H160 A34,34 0 0 0 122,912 V292 A34,34 0 0 0 160,254 Z"
          fill="none" stroke="var(--frame-soft)" stroke-width="2.5"/>
  </svg>

  <p class="greeting greeting--merry">Merry</p>
  <p class="greeting greeting--christmas">Christmas</p>
  <p class="greeting greeting--and">&amp;</p>
  <p class="greeting greeting--newyear">Happy New Year</p>

  <div class="signature">
    <span class="signature__year">2016</span>
    <span class="signature__dot"></span>
    <span class="signature__name">lumo.</span>
  </div>

  <svg class="card__florals" viewBox="0 0 840 1200">
    <defs>
      <linearGradient id="floral-top" x1="0" y1="0" x2="1" y2="1">
        <stop offset="0" stop-color="var(--leaf)" stop-opacity="0.85"/>
        <stop offset="0.55" stop-color="var(--petal)" stop-opacity="0.85"/>
        <stop offset="1" stop-color="var(--bloom)" stop-opacity="0.75"/>
      </linearGradient>
      <linearGradient id="floral-bottom" x1="1" y1="1" x2="0" y2="0">
        <stop offset="0" stop-color="var(--leaf)" stop-opacity="0.85"/>
        <stop offset="0.55" stop-color="var(--petal)" stop-opacity="0.85"/>
        <stop offset="1" stop-color="var(--bloom)" stop-opacity="0.75"/>
      </linearGradient>
    </defs>
    <path role="img" aria-label="Illustrated cluster of hibiscus flowers, pink blossoms and tropical leaves in the top left corner"
          fill="url(#floral-top)"
          d="M40,60 C90,10 200,20 290,50 C360,70 480,60 500,110 C515,150 440,170 380,180 C320,200 300,260 250,300 C200,340 140,350 90,330 C40,310 10,250 30,190 C45,140 10,100 40,60 Z"/>
    <path role="img" aria-label="Illustrated cluster of hibiscus flowers, pink blossoms and tropical leaves in the bottom right corner"
          fill="url(#floral-bottom)"
          d="M800,1150 C750,1190 640,1185 550,1160 C470,1140 380,1150 370,1100 C360,1060 440,1040 500,1020 C560,1000 580,930 630,890 C680,850 740,830 790,850 C840,870 830,940 815,1000 C805,1050 840,1100 800,1150 Z"/>
  </svg>
</main>
</body>
</html>
```